Harrowgate Lending Inc. Investor Presentation

We would like a PowerPoint presentation to attract prospective investors. It needs to look extremely professional since we are a financial lending institution, and seeking capital investors. We specialize in Private Lending with Mortgage Backed Securities, both Residential and Commercial properties.

```html
<!DOCTYPE html>
<html lang="en">
<head>
<meta charset="utf-8">
<title>Harrowgate Lending Inc. – Investor Presentation</title>
<link rel="stylesheet" href="https://fonts.googleapis.com/css2?family=Cormorant+Garamond:wght@500&family=Plus+Jakarta+Sans:wght@600;700&display=swap">
<style>
  :root {
    --board: #e0e0e0;
    --navy: #26266b;
    --navy-deep: #1f2552;
    --indigo: #3a3579;
    --gold: #e8c547;
    --gold-soft: #e2c04a;
    --ink: #111111;
    --white: #ffffff;
    --serif: "Cormorant Garamond", serif;
    --sans: "Plus Jakarta Sans", sans-serif;
  }
  * { margin: 0; padding: 0; box-sizing: border-box; }
  html, body { width: 1200px; height: 751px; overflow: hidden; background: var(--board); }
  .board { position: relative; width: 1200px; height: 751px; }
  .slide { position: absolute; width: 514px; height: 289px; overflow: hidden; background: var(--white); }
  .slide--cover { left: 76px; top: 72px; }
  .slide--about { left: 630px; top: 72px; }
  .slide--approach { left: 76px; top: 382px; background: var(--navy); }
  .slide--contact { left: 630px; top: 382px; }

  .wordmark { font-family: var(--serif); font-weight: 500; text-transform: uppercase; line-height: 1; text-align: center; }

  /* Cover */
  .cover__brand { position: absolute; left: 0; top: 0; width: 254px; height: 289px; }
  .cover__mark { position: absolute; left: 117px; top: 88px; width: 20px; height: 20px; background: var(--gold); }
  .cover__name { position: absolute; left: 0; top: 148px; width: 254px; font-size: 29px; letter-spacing: 0.5px; color: var(--ink); }
  .cover__name span { display: block; margin-bottom: 4px; }
  .cover__tagline { position: absolute; left: 0; top: 248px; width: 254px; text-align: center; font-family: var(--sans); font-weight: 700; font-size: 11.5px; letter-spacing: 0.3px; color: var(--ink); }
  .cover__panel { position: absolute; left: 254px; top: 0; width: 260px; height: 289px; background: var(--gold-soft); }

  /* About */
  .about__band { position: absolute; left: 0; top: 0; }
  .about__logo { position: absolute; right: 20px; top: 19px; font-size: 10.5px; color: var(--indigo); text-align: left; }
  .about__copy { position: absolute; left: 20px; top: 56px; width: 348px; font-family: var(--sans); font-weight: 600; font-size: 9.6px; line-height: 15.4px; color: var(--ink); text-align: justify; }
  .about__copy p + p { margin-top: 18px; }
  .about__photo { position: absolute; left: 0; top: 199px; width: 514px; height: 90px; background: linear-gradient(100deg, var(--navy-deep) 0%, #3b4170 55%, var(--navy-deep) 100%); }
  .about__caption { position: absolute; left: 0; top: 265px; width: 514px; text-align: center; font-family: var(--sans); font-weight: 700; font-size: 12.4px; letter-spacing: 0.3px; color: var(--white); }

  /* Approach */
  .approach__wedge { position: absolute; left: 0; top: 0; }
  .approach__copy { position: absolute; left: 25px; top: 39px; width: 238px; font-family: var(--sans); font-weight: 600; font-size: 9.6px; line-height: 15.4px; color: var(--white); text-align: justify; text-align-last: left; }
  .approach__accent { position: absolute; left: 0; top: 0; }
  .approach__photo { position: absolute; left: 352px; top: 42px; width: 120px; height: 165px; background: linear-gradient(160deg, #c9a98a 0%, #b8b8b8 35%, #d6dadd 70%, #eef0f2 100%); box-shadow: 8px 10px 14px rgba(0,0,0,0.35); }
  .approach__ornament { position: absolute; left: 26px; top: 164px; width: 64px; height: 64px; background: rgba(232,197,71,0.18); }
  .approach__logo { position: absolute; left: 21px; top: 248px; font-size: 9.5px; color: var(--indigo); text-align: left; }

  /* Contact */
  .contact__photo { position: absolute; inset: 0; background: radial-gradient(ellipse at 50% 45%, #47448a 0%, var(--indigo) 55%, #2e2a66 100%); }
  .contact__mark { position: absolute; left: 249px; top: 60px; width: 16px; height: 16px; background: var(--gold); }
  .contact__name { position: absolute; left: 0; top: 116px; width: 514px; font-size: 26px; color: var(--white); }
  .contact__name span { display: block; margin-bottom: 3px; }
  .contact__address { position: absolute; left: 0; top: 190px; width: 514px; text-align: center; font-family: var(--sans); font-weight: 700; font-size: 9.8px; line-height: 15.4px; color: var(--white); font-style: normal; }
</style>
</head>
<body>
<main class="board">

  <section class="slide slide--cover">
    <div class="cover__brand">
      <div class="cover__mark"></div>
      <h1 class="wordmark cover__name"><span>Harrowgate</span><span>Lending</span></h1>
      <p class="cover__tagline">PERFORM - PROTECT - PROSPER</p>
    </div>
    <div class="cover__panel" role="img" aria-label="Gold textured background with faint lettering and a large geometric pattern"></div>
  </section>

  <section class="slide slide--about">
    <svg class="about__band" width="514" height="34" viewBox="0 0 514 34" aria-hidden="true">
      <polygon points="0,0 410,0 385,32 0,32" fill="var(--navy-deep)"/>
    </svg>
    <div class="wordmark about__logo">Harrowgate<br>Lending</div>
    <div class="about__copy">
      <p>Harrowgate Lending Inc. is a leading private investor and business accelerator that leverages the experience, insights, and resources of its founder, Mr. Daniel R. Whitcombe, an accomplished entrepreneur and investor.</p>
      <p>Harrowgate Lending Inc. has been investing its own capital since 1998 and has had a prestigious track record generating over $2 Billion in enterprise value across various industries including financial services, software, biotechnology, advanced manufacturing, and alternative energy.</p>
    </div>
    <div class="about__photo" role="img" aria-label="Navy-tinted photo of hands counting banknotes"></div>
    <p class="about__caption">RESIDENTIAL AND COMMERCIAL PROPERTIES.</p>
  </section>

  <section class="slide slide--approach">
    <svg class="approach__wedge" width="514" height="289" viewBox="0 0 514 289" aria-hidden="true">
      <polygon points="0,202 514,158 514,289 0,289" fill="var(--white)"/>
    </svg>
    <p class="approach__copy">The entrepreneurial heritage and innovative spirit of the firm allows it to take unconventional and creative approaches to investing, that are often contrarian and sometimes pioneering.</p>
    <svg class="approach__accent" width="514" height="289" viewBox="0 0 514 289" aria-hidden="true">
      <polygon points="496,182 486,211 439,239 451,209" fill="var(--gold)"/>
    </svg>
    <div class="approach__photo" role="img" aria-label="Photo of a small model house on architectural plans with a magnifying glass"></div>
    <div class="approach__ornament" role="img" aria-label="Gold geometric line ornament"></div>
    <div class="wordmark approach__logo">Harrowgate<br>Lending</div>
  </section>

  <section class="slide slide--contact">
    <div class="contact__photo" role="img" aria-label="Indigo-tinted photo of hands typing on a laptop showing a dashboard"></div>
    <div class="contact__mark"></div>
    <h2 class="wordmark contact__name"><span>Harrowgate</span><span>Lending</span></h2>
    <address class="contact__address">
      Kingsmere Plaza, Harbour Tower<br>
      240 Front Street, Suite 1910<br>
      Toronto, ON M5V 1K4<br>
      Tel: 416-555-0148
    </address>
  </section>

</main>
</body>
</html>
```